Website Design for Law Firm

We need a fresh new website design for our client 'Torvek Legal' who specialises as a Criminal, Traffic & Civil Lawyer in Perth, Western Australia. We are looking for a very clean, professional and elegant look for the website, a presence of power and class needed as he deals with high end clients. Black, Silver and hints of gold need to run through the design without making the site look too dark. We are after a very modern, spacious web look, use of large readable text with links to social media (such as Facebook, Google+, Twitter, LinkedIn) to stand out and his contact details to be made very predominate.

Reason: Public holidays here in Australia, need more business hours to discuss designs with client.

Reason: Client needs more time to look through designs.

Reason: Client is going over last of designs. Design will be picked early next week!

Law Firm

```html
<!DOCTYPE html>
<html lang="en">
<head>
<meta charset="utf-8">
<title>Torvek Legal</title>
<link href="https://fonts.googleapis.com/css2?family=Questrial&family=Open+Sans:wght@400;600&display=swap" rel="stylesheet">
<style>
:root{
  --gold:#c9a30f;
  --gold-dark:#a8850a;
  --ink:#222;
  --text:#5a5a5a;
  --charcoal:#2b2b2b;
  --charcoal-2:#3a3a3a;
  --paper:#efefef;
  --rule:#d6d6d6;
  --white:#fff;
}
*{margin:0;padding:0;box-sizing:border-box}
html,body{width:1200px;height:2225px;overflow:hidden}
body{position:relative;background:var(--white);font-family:"Open Sans",sans-serif;color:var(--text)}
.abs{position:absolute}
.head-font{font-family:"Questrial",sans-serif}

/* header */
.top-line{left:0;top:0;width:1200px;height:4px;background:var(--gold)}
.header{left:0;top:4px;width:1200px;height:141px;background:linear-gradient(#fafafa,#e6e6e6);border-bottom:3px solid var(--charcoal)}
.brand{left:72px;top:44px;font-family:"Questrial",sans-serif;font-size:40px;letter-spacing:2px;color:var(--ink);line-height:1}
.brand small{display:block;font-size:19px;letter-spacing:9px;margin-top:6px;padding-left:70px}
.social-top{left:836px;top:38px;display:flex;gap:8px}
.dot{width:26px;height:26px;border-radius:50%;background:#3e6fb3}
.dot.sky{background:#3fa6dc}.dot.blue{background:#1b75bb}
.search{left:945px;top:36px;width:212px;height:32px;border:1px solid #c9c9c9;border-radius:16px;background:var(--white);font-size:13px;color:#777;padding:7px 16px;font-family:"Questrial",sans-serif}
.search svg{position:absolute;right:12px;top:8px}
.nav{left:318px;top:95px;width:882px;height:50px;background:linear-gradient(#333,#1d1d1d);clip-path:polygon(18px 0,100% 0,100% 100%,0 100%)}
.nav ul{list-style:none;display:flex;gap:0;margin-left:34px;height:100%;align-items:center}
.nav li{font-family:"Questrial",sans-serif;color:var(--white);font-size:14px;letter-spacing:1px;margin-right:41px}

/* hero */
.hero{left:0;top:148px;width:1200px;height:472px;background:linear-gradient(100deg,#cfd4d8 0%,#eef0f1 45%,#e2e6e8 100%);border-bottom:1px solid #999}
.hero-photo{left:60px;top:160px;width:700px;height:460px;background:radial-gradient(ellipse at 40% 45%,#4a4d55 0%,#6b6f78 35%,rgba(200,205,210,0) 70%)}
.case-form{left:783px;top:187px;width:333px;height:380px;background:linear-gradient(#3d3d3d,#262626);clip-path:polygon(0 0,100% 0,100% 340px,50% 100%,0 340px)}
.case-form h2{height:45px;background:linear-gradient(#d9b626,var(--gold-dark));color:var(--white);font-family:"Questrial",sans-serif;font-size:23px;font-weight:400;text-align:center;line-height:45px;letter-spacing:1px}
.field{position:absolute;background:var(--white);border-radius:3px;font-size:13px;color:#888;padding:8px 10px;height:30px}
.submit{position:absolute;left:76px;top:287px;width:182px;height:38px;background:linear-gradient(#dcba2e,#a8850a);border-radius:4px;color:var(--white);font-family:"Questrial",sans-serif;font-size:17px;letter-spacing:1px;text-align:center;line-height:38px}

/* practice */
.practice{left:0;top:621px;width:1200px;height:676px;background:var(--paper)}
.section-title{font-family:"Questrial",sans-serif;font-size:22px;letter-spacing:1px;color:var(--ink)}
.section-title span{color:var(--gold)}
.area h3{font-family:"Questrial",sans-serif;font-weight:400;font-size:18px;letter-spacing:1px;color:var(--ink);margin-bottom:8px}
.area p{font-size:14px;line-height:20px;color:var(--text);width:325px}
.area a{font-size:13px;color:var(--gold);text-decoration:none}
.v-rule{left:599px;top:708px;width:1px;height:455px;background:var(--rule)}
.h-rule{left:70px;top:930px;width:1060px;height:1px;background:var(--rule)}
.btn-dark{background:linear-gradient(#3a3a3a,#1c1c1c);border-bottom:3px solid var(--gold);color:var(--white);font-family:"Questrial",sans-serif;text-align:center;letter-spacing:1px}

/* welcome + cases */
.welcome p{font-size:14.5px;line-height:21px;width:462px;margin-bottom:21px}
.rule{height:1px;background:var(--rule)}
.case{display:flex;gap:12px;width:470px}
.thumb{width:128px;height:86px;border:3px solid #ccc;flex:none}
.case h4{font-family:"Questrial",sans-serif;font-weight:400;font-size:17px;color:var(--ink);margin-bottom:2px}
.case p{font-size:13.5px;line-height:19px}

/* footer */
.foot-band{left:0;top:1868px;width:1200px;height:8px;background:var(--gold)}
.footer{left:0;top:1876px;width:1200px;height:304px;background:linear-gradient(#3c3c3c,#232323)}
.foot-h{font-family:"Questrial",sans-serif;font-size:16px;letter-spacing:1px;color:var(--white)}
.foot-rule{height:1px;background:#555}
.links{list-style:none;font-size:13.5px;color:#ddd;line-height:23.5px;font-family:"Questrial",sans-serif}
.fdot{width:22px;height:22px;border-radius:50%;background:var(--white)}
.card{width:84px;height:55px;border-radius:5px;font-family:"Questrial",sans-serif;font-size:15px;text-align:center;line-height:55px}
.copy{left:0;top:2180px;width:1200px;height:45px;background:#141414;color:#ddd;font-family:"Questrial",sans-serif;font-size:13.5px;text-align:center;line-height:45px}
</style>
</head>
<body>

<div class="abs top-line"></div>
<header class="abs header"></header>
<div class="abs brand">TORVEK<small>LEGAL</small></div>
<div class="abs social-top" aria-label="Social links"><span class="dot"></span><span class="dot sky"></span><span class="dot blue"></span></div>
<div class="abs search">Keyword Search
  <svg width="14" height="14" viewBox="0 0 14 14"><circle cx="5.5" cy="5.5" r="4" fill="none" stroke="#aaa" stroke-width="1.6"/><line x1="8.5" y1="8.5" x2="13" y2="13" stroke="#aaa" stroke-width="1.8"/></svg>
</div>
<nav class="abs nav"><ul><li>HOME</li><li>ABOUT US</li><li>PRACTICE AREAS</li><li>SCOPE OF ADVICE</li><li>LEGAL COST</li><li>PRESS</li><li>CONTACT</li></ul></nav>

<section class="abs hero"></section>
<div class="abs hero-photo" role="img" aria-label="Photo of a lawyer in a suit working at a desk with a scales of justice statue"></div>
<form class="abs case-form">
  <h2>• Free Case Assesment •</h2>
  <div class="field" style="left:18px;top:77px;width:144px">Firstname</div>
  <div class="field" style="left:171px;top:77px;width:145px">Lastname</div>
  <div class="field" style="left:18px;top:121px;width:144px">Phone no.</div>
  <div class="field" style="left:171px;top:121px;width:145px">Email</div>
  <div class="field" style="left:18px;top:166px;width:298px;height:101px">Message...</div>
  <div class="submit">SUBMIT</div>
</form>

<section class="abs practice"></section>
<h2 class="abs section-title" style="left:0;top:645px;width:1200px;text-align:center">PRACTICE <span>AREAS</span></h2>
<div class="abs v-rule"></div>
<div class="abs h-rule"></div>

<svg class="abs" style="left:70px;top:755px" width="124" height="100" viewBox="0 0 124 100" aria-hidden="true">
  <g fill="none" stroke="#c9a30f" stroke-width="10"><circle cx="30" cy="35" r="20"/><circle cx="92" cy="62" r="20"/><path d="M46 40 Q62 46 74 52"/></g>
</svg>
<div class="abs area" style="left:228px;top:738px"><h3>CRIMINAL LAW</h3><p>Lorem ipsum dolor sit amet, consectetur adipiscing elit. Fusce vestibulum dui vitae tincidunt, a placerat ipsum feugiat. Aliquam adipiscing consectetur tellus interdum ui vitae tincidunt a placerat.</p><a>Read more ›</a></div>

<svg class="abs" style="left:640px;top:750px" width="124" height="110" viewBox="0 0 124 110" aria-hidden="true">
  <g fill="#c9a30f"><rect x="58" y="8" width="8" height="80"/><rect x="10" y="18" width="104" height="6"/><rect x="36" y="88" width="52" height="12" rx="3"/><path d="M2 60 h40 a20 14 0 0 1 -40 0z"/><path d="M82 60 h40 a20 14 0 0 1 -40 0z"/><circle cx="62" cy="8" r="7"/></g>
  <g stroke="#c9a30f" stroke-width="2"><line x1="14" y1="24" x2="4" y2="60"/><line x1="14" y1="24" x2="40" y2="60"/><line x1="110" y1="24" x2="84" y2="60"/><line x1="110" y1="24" x2="120" y2="60"/></g>
</svg>
<div class="abs area" style="left:795px;top:738px"><h3>CIVIL LAW</h3><p>Lorem ipsum dolor sit amet, consectetur adipiscing elit. Fusce vestibulum dui vitae tincidunt, a placerat ipsum feugiat. Aliquam adipiscing consectetur tellus interdum ui vitae tincidunt a placerat.</p><a>Read more ›</a></div>

<svg class="abs" style="left:90px;top:983px" width="80" height="114" viewBox="0 0 80 114" aria-hidden="true">
  <g fill="#c9a30f"><rect x="14" y="0" width="52" height="114" rx="8"/><path d="M0 8h14v18zM80 8h-14v18zM0 44h14v18zM80 44h-14v18z"/></g>
  <g fill="#e7cf6b"><circle cx="40" cy="22" r="12"/><circle cx="40" cy="57" r="12"/><circle cx="40" cy="92" r="12"/></g>
</svg>
<div class="abs area" style="left:228px;top:965px"><h3>TRAFFIC LAW</h3><p>Lorem ipsum dolor sit amet, consectetur adipiscing elit. Fusce vestibulum dui vitae tincidunt, a placerat ipsum feugiat. Aliquam adipiscing consectetur tellus interdum ui vitae tincidunt a placerat.</p><a>Read more ›</a></div>

<svg class="abs" style="left:640px;top:983px" width="120" height="112" viewBox="0 0 120 112" aria-hidden="true">
  <g fill="#c9a30f"><path d="M60 0 L118 30 H2z"/><rect x="8" y="32" width="104" height="8"/><rect x="16" y="46" width="14" height="50"/><rect x="40" y="46" width="14" height="50"/><rect x="66" y="46" width="14" height="50"/><rect x="90" y="46" width="14" height="50"/><rect x="6" y="98" width="108" height="6"/><rect x="0" y="106" width="120" height="6"/></g>
</svg>
<div class="abs area" style="left:795px;top:965px"><h3>COURT WORK</h3><p>Lorem ipsum dolor sit amet, consectetur adipiscing elit. Fusce vestibulum dui vitae tincidunt, a placerat ipsum feugiat. Aliquam adipiscing consectetur tellus interdum ui vitae tincidunt a placerat.</p><a>Read more ›</a></div>

<div class="abs btn-dark" style="left:509px;top:1187px;width:180px;height:44px;line-height:41px;font-size:17px">VIEW ALL</div>

<h2 class="abs section-title" style="left:86px;top:1353px">WELCOME TO <span>TORVEK LEGAL</span></h2>
<div class="abs rule" style="left:86px;top:1403px;width:475px"></div>
<div class="abs welcome" style="left:88px;top:1430px;height:320px;overflow:hidden">
  <p>Torvek Legal is an established Law firm specialising in Criminal Law, Traffic Law and Civil Law. Dr Aldous Wren is the firm's Legal Practitioner Director.</p>
  <p>Aldous is an experienced Legal Advocate dedicated to protecting you legal rights.</p>
  <p>In the last two years he has notched up over 2,000 appearances in the Magistrates Court, District Court, Supreme Court and Children's Court.</p>
  <p>Aldous was formerly with the Public Counsel Office of WA Criminal Division and before that he enjoyed a long and successful international career with various agencies of the Meridian Council. He has taught Criminal Law and Advanced Criminal Law</p>
</div>
<div class="abs btn-dark" style="left:85px;top:1771px;width:136px;height:36px;line-height:33px;font-size:14px">Read more</div>

<h2 class="abs section-title" style="left:643px;top:1353px">RECENT <span>CASES</span></h2>
<div class="abs rule" style="left:643px;top:1403px;width:467px"></div>
<div class="abs case" style="left:648px;top:1425px"><div class="thumb" role="img" aria-label="Photo of a business handshake" style="background:linear-gradient(135deg,#1d2430,#5a6270)"></div><div><h4>Article Title goes here</h4><p>Lorem ipsum dolor sit amet, consectetur adipiscing elit. Phasellus eget leo leo. Sed adipiscing mi orci, vel ultrices turpis mattis a.</p></div></div>
<div class="abs case" style="left:648px;top:1541px"><div class="thumb" role="img" aria-label="Photo of a judge's gavel on banknotes" style="background:linear-gradient(135deg,#3a1f0e,#9a6a35)"></div><div><h4>Article Title goes here</h4><p>Lorem ipsum dolor sit amet, consectetur adipiscing elit. Phasellus eget leo leo. Sed adipiscing mi orci, vel ultrices turpis mattis a.</p></div></div>
<div class="abs case" style="left:648px;top:1658px"><div class="thumb" role="img" aria-label="Photo of a hand signing a document" style="background:linear-gradient(135deg,#c8b89a,#6e5a40)"></div><div><h4>Article Title goes here</h4><p>Lorem ipsum dolor sit amet, consectetur adipiscing elit. Phasellus eget leo leo. Sed adipiscing mi orci, vel ultrices turpis mattis a.</p></div></div>

<div class="abs foot-band"></div>
<footer class="abs footer"></footer>
<h3 class="abs foot-h" style="left:101px;top:1927px">QUICKLINKS</h3>
<div class="abs foot-rule" style="left:101px;top:1961px;width:247px"></div>
<ul class="abs links" style="left:108px;top:1973px"><li>Home</li><li>About</li><li>Practice Areas</li><li>Scope of Advice</li></ul>
<ul class="abs links" style="left:246px;top:1973px"><li>Legal Cost</li><li>Recent Cases</li><li>Press</li><li>Contact</li></ul>
<div class="abs" style="left:107px;top:2086px;display:flex;gap:7px"><span class="fdot"></span><span class="fdot"></span><span class="fdot"></span><span class="fdot"></span></div>

<h3 class="abs foot-h" style="left:457px;top:1927px">USEFUL INFORMATION</h3>
<div class="abs foot-rule" style="left:457px;top:1961px;width:211px"></div>
<ul class="abs links" style="left:464px;top:1973px"><li>Sitemap</li><li>F.A.Q</li><li>Service Policy</li><li>Terms &amp; Conditions</li></ul>

<h3 class="abs foot-h" style="left:769px;top:1927px">FOR YOUR CONVENIECE WE ACCEPT:</h3>
<div class="abs foot-rule" style="left:769px;top:1961px;width:347px"></div>
<div class="abs card" style="left:787px;top:2000px;background:#f4f4f4;color:#333">Cardline</div>
<div class="abs card" style="left:899px;top:2000px;background:#f4f4f4;color:#333">Paywell</div>
<div class="abs card" style="left:1010px;top:2000px;background:#b32025;color:#fff">Tapnet</div>
<div class="abs" style="left:769px;top:2082px;width:347px;text-align:center;font-family:'Questrial',sans-serif;font-size:11px;color:#eee;letter-spacing:.5px">ALL MAJOR CREDIT CARDS ARE ACCEPTED</div>

<div class="abs copy">Copyright 2014 Torvek Legal &nbsp;All rights</div>

</body>
</html>
```